Westerly Open Cinema Showcase 20th Annual Poster

September 2017 will to the 20th Annual Westerly Open Cinema Showcase. We have a new logo and need a new modern stylish poster designed. One that shows creativity, imagination, style and class. Think outside the box. Modern and new.

Dates are: September 7th - 13th 2017

Our tagline:
"Something for Everyone from Around the World"

Target Market(s)

film festival goings - 35 - 70 age range - 58% female 42% males - movie lovers - movie goers

Industry/Entity Type

Movie

Font styles to use
Script

Requirements
Must have
• modern style celebrating 20 years - cool design - chic and stylish - upscale - high society - think Abstract
Nice to have
• thinking outside the box - not just simple film reel - think Abstract! Not just your standard film items. Creative in your idea and design
Should not have
• no CLIP ART

```html
<!DOCTYPE html>
<html lang="en">
<head>
<meta charset="utf-8">
<title>Westerly Open Cinema Showcase – 20th Annual</title>
<link rel="stylesheet" href="https://fonts.googleapis.com/css2?family=Anton&family=Damion&display=swap">
<style>
  :root {
    --festival-red: #ec1c24;
    --ink: #000000;
    --paper: #ffffff;
    --perforation: #fbf6c8;
    --badge-navy: #17214a;
    --headline-font: "Anton", sans-serif;
    --script-font: "Damion", cursive;
  }
  html, body {
    margin: 0;
    padding: 0;
    overflow: hidden;
    background: var(--paper);
  }
  .poster {
    position: relative;
    width: 810px;
    height: 1200px;
    overflow: hidden;
    background: var(--festival-red);
  }
  .film-edge {
    position: absolute;
    top: 0;
    height: 1200px;
    background-color: var(--ink);
    background-image: linear-gradient(to bottom, var(--perforation) 0 16px, transparent 16px 60px);
    background-size: 38px 60px;
    background-repeat: repeat-y;
  }
  .film-edge--left { left: 0; width: 56px; background-position: 7px 0; }
  .film-edge--right { left: 756px; width: 54px; background-position: 10px 0; }

  .projection-beam {
    position: absolute;
    left: 0;
    top: 0;
  }

  .projector-art {
    position: absolute;
    left: 56px;
    top: 700px;
    width: 414px;
    height: 500px;
    border-radius: 110px 110px 0 0;
    background: radial-gradient(circle at 60% 30%, #2a0506 0%, #000000 70%);
  }

  .title {
    position: absolute;
    left: 104px;
    top: 108px;
    margin: 0;
    font-family: var(--headline-font);
    font-weight: 400;
    font-size: 80px;
    line-height: 96px;
    letter-spacing: 2px;
  }
  .title__line { display: block; color: var(--ink); white-space: nowrap; }
  .title__line--light { color: var(--paper); }

  .anniversary-badge {
    position: absolute;
    left: 492px;
    top: 0;
    width: 240px;
    height: 240px;
  }
  .anniversary-badge__text {
    position: absolute;
    left: 0;
    top: 44px;
    width: 240px;
    text-align: center;
    font-family: var(--headline-font);
    font-size: 54px;
    line-height: 64px;
    color: var(--ink);
  }

  .tagline {
    position: absolute;
    left: 85px;
    top: 444px;
    width: 640px;
    margin: 0;
    transform: rotate(-14deg);
    transform-origin: center;
    font-family: var(--script-font);
    font-weight: 400;
    font-size: 60px;
    line-height: 92px;
    color: var(--paper);
    text-align: center;
    white-space: nowrap;
  }
  .tagline__line { display: block; }
  .tagline__line--second { padding-left: 30px; }

  .star { position: absolute; }
  .star--right { left: 678px; top: 444px; width: 64px; height: 64px; }
  .star--left { left: 70px; top: 566px; width: 60px; height: 60px; }

  .dates {
    position: absolute;
    left: 480px;
    top: 872px;
    width: 258px;
    margin: 0;
    text-align: center;
    font-family: var(--headline-font);
    font-weight: 400;
    color: var(--paper);
    font-size: 62px;
    line-height: 68px;
  }

  .festival-mark {
    position: absolute;
    left: 420px;
    top: 1056px;
    width: 136px;
    height: 136px;
    border-radius: 50%;
    background: var(--badge-navy);
    display: flex;
    align-items: center;
    justify-content: center;
    font-family: var(--headline-font);
    font-size: 34px;
    letter-spacing: 2px;
    color: var(--paper);
  }
</style>
</head>
<body>
<main class="poster">
  <svg class="projection-beam" width="810" height="1200" viewBox="0 0 810 1200" aria-hidden="true">
    <polygon points="472,896 756,688 756,1200 724,1200 472,1016" fill="var(--ink)"/>
  </svg>

  <div class="film-edge film-edge--left"></div>
  <div class="film-edge film-edge--right"></div>

  <div class="projector-art" role="img" aria-label="Black silhouette of a vintage film projector with two red-spoked reels on a tripod"></div>

  <h1 class="title">
    <span class="title__line">Westerly</span>
    <span class="title__line title__line--light">Open Cinema</span>
    <span class="title__line">Showcase</span>
  </h1>

  <div class="anniversary-badge">
    <svg width="240" height="240" viewBox="-120 -120 240 240" aria-hidden="true">
      <polygon fill="var(--paper)" points="0,-120 22,-92 56,-106 62,-72 98,-70 88,-36 118,-20 94,6 114,34 82,44 86,80 50,80 36,114 8,94 -22,118 -40,88 -76,96 -78,60 -112,46 -94,18 -118,-10 -88,-30 -102,-64 -66,-70 -60,-106 -28,-92"/>
    </svg>
    <div class="anniversary-badge__text">20th<br>Annual</div>
  </div>

  <p class="tagline">
    <span class="tagline__line">Something for Everyone</span>
    <span class="tagline__line tagline__line--second">from Around the World</span>
  </p>

  <svg class="star star--right" viewBox="0 0 24 24" aria-hidden="true">
    <polygon fill="var(--paper)" points="12,1 15,9 23,9 16.5,14 19,22 12,17 5,22 7.5,14 1,9 9,9"/>
  </svg>
  <svg class="star star--left" viewBox="0 0 24 24" aria-hidden="true">
    <polygon fill="var(--paper)" points="12,1 15,9 23,9 16.5,14 19,22 12,17 5,22 7.5,14 1,9 9,9"/>
  </svg>

  <p class="dates">7 - 13.<br>SEPT/2017</p>

  <div class="festival-mark">WOCS</div>
</main>
</body>
</html>
```